Real Estate Sign 2

Our company is called Corwin Hadley Realty. We are a real estate development company. We need a sign that we are going to hang outside of our projects that says: Another project brought to you by Corwin Hadley Realty... For Sale....(213) 555-0187. At the very bottom is needs to say CaBRE# 04637251" We want the Corwin Hadley Realty to be sophisticated, fresh, simple. We do not have a logo so maybe one can be incorporated into the sign. Sign will be about 30"x24"

Industry/Entity Type

Real Estate

```html
<!DOCTYPE html>
<html lang="en">
<head>
<meta charset="utf-8">
<title>Corwin Hadley Realty – For Sale Sign</title>
<link rel="stylesheet" href="https://fonts.googleapis.com/css2?family=Arimo:wght@400;700&family=Crimson+Pro:wght@700&display=swap">
<style>
  :root {
    --sign-red: #c20e1a;
    --sign-charcoal: #222222;
    --sign-slate: #3d3d3d;
    --sign-white: #ffffff;
  }
  html, body {
    margin: 0;
    padding: 0;
    width: 1200px;
    height: 960px;
    overflow: hidden;
    background: var(--sign-charcoal);
  }
  .sign {
    position: relative;
    width: 1200px;
    height: 960px;
    background: var(--sign-charcoal);
    color: var(--sign-white);
    font-family: "Arimo", Helvetica, Arial, sans-serif;
    overflow: hidden;
  }
  .sign__backdrop {
    position: absolute;
    inset: 0;
    width: 1200px;
    height: 960px;
  }
  .sign__header-band {
    position: absolute;
    left: 0;
    top: 0;
    width: 1200px;
    height: 110px;
    background: var(--sign-red);
  }
  .sign__footer-band {
    position: absolute;
    left: 0;
    top: 885px;
    width: 920px;
    height: 75px;
    background: var(--sign-red);
  }
  .sign__text {
    position: absolute;
    margin: 0;
    line-height: 1;
    white-space: nowrap;
  }
  .tagline {
    left: 26px;
    top: 36px;
    font-size: 50px;
    font-weight: 400;
    letter-spacing: 2.2px;
  }
  .brand-name {
    left: 26px;
    font-family: "Crimson Pro", Georgia, "Times New Roman", serif;
    font-weight: 700;
    font-size: 168px;
    letter-spacing: 1px;
  }
  .brand-name--first { top: 148px; }
  .brand-name--second { top: 298px; }
  .brand-descriptor {
    left: 28px;
    top: 464px;
    font-size: 72px;
    font-weight: 400;
    letter-spacing: 2px;
  }
  .status {
    left: 26px;
    top: 615px;
    font-size: 112px;
    font-weight: 700;
  }
  .phone {
    left: 24px;
    top: 721px;
    font-size: 82px;
    font-weight: 700;
  }
  .license {
    left: 26px;
    top: 912px;
    font-size: 36px;
    font-weight: 400;
    letter-spacing: 0.5px;
  }
</style>
</head>
<body>
  <main class="sign">
    <svg class="sign__backdrop" viewBox="0 0 1200 960" aria-hidden="true">
      <polygon class="sign__roofline" points="1200,112 1200,960 920,960 920,712 668,712" fill="var(--sign-slate)"/>
    </svg>

    <div class="sign__header-band"></div>
    <p class="sign__text tagline">ANOTHER PROJECT BROUGHT TO YOU BY</p>

    <h1 class="sign__text brand-name brand-name--first">CORWIN</h1>
    <p class="sign__text brand-name brand-name--second">HADLEY</p>
    <p class="sign__text brand-descriptor">REALTY</p>

    <p class="sign__text status">FOR SALE</p>
    <p class="sign__text phone">(213) 555-0187</p>

    <div class="sign__footer-band"></div>
    <p class="sign__text license">CaBRE# 04637251</p>
  </main>
</body>
</html>
```